Facebook cover photo and Icon- Pet Related

I am looking to have a few custom cover photos designed for my business Facebook page so I can rotate between them every month.

We are a start up pet product delivery service for our local market. We specialize in dog and cat food and treats.

We want our Facebook page to have the same feel as our website to solidify our brand. Our work in progress website is www.brisktailcourier.com. Please not this is still a work in progress and some of the photos may be changing.

Each cover photo have a different look and feel however should still relate to our brand.

We would like 3 cover photos created with a 'theme' around each of the following phrases. Each saying should also be included on the photo itself.

1. You can't buy happiness, but you can buy local and that's kind of the same thing.
3. Sit. Stay. Let us fetch!
4. Making your life easier, theirs healthier and happier.

We are open to dog, cat, and people 'stock' photos being included as long as the photo goes with the saying.

In addition to the cover photos we would like a design for our 'profile photo' as well.

I am including our logos for you to use as needed.

Industry/Entity Type

Delivery Service

Requirements
Must have
• We would like the text over a photo of people with cats and dogs.
Nice to have
• If there is no photos of humans with cats and dogs the next best thing would be a graphic that goes with the text.
Should not have
• Not interested in designs with animated animals.

```html
<!DOCTYPE html>
<html lang="en">
<head>
<meta charset="utf-8">
<title>BriskTail – Making your life easier, theirs healthier and happier</title>
<link rel="stylesheet" href="https://fonts.googleapis.com/css2?family=Sansita:ital,wght@0,800;1,800&family=Open+Sans:wght@300;400&display=swap">
<style>
  :root {
    --paper: #ffffff;
    --mint: #a3f3e2;
    --sun: #f7e200;
    --tangerine: #f26a1f;
    --lime: #a8e21c;
    --slate: #a9b1b7;
    --stone: #c4ccca;
    --logo-grey: #7c8387;
    --rope-light: #c9a27a;
    --rope-dark: #9a7350;
    --fur-light: #d9d9dc;
    --fur-dark: #9c9ea3;
  }
  * { margin: 0; padding: 0; box-sizing: border-box; }
  html, body { width: 1200px; height: 601px; overflow: hidden; background: var(--paper); }
  .cover {
    position: relative;
    width: 1200px;
    height: 601px;
    background: var(--paper);
    overflow: hidden;
  }
  .rope-photo, .kitten-photo { position: absolute; left: 0; top: 0; }
  .slogan { position: absolute; inset: 0; }
  .slogan span { position: absolute; line-height: 1; white-space: nowrap; }
  .display { font-family: "Sansita", "Trebuchet MS", sans-serif; font-weight: 800; }
  .display-italic { font-family: "Sansita", "Trebuchet MS", sans-serif; font-weight: 800; font-style: italic; }
  .light { font-family: "Open Sans", Arial, sans-serif; font-weight: 300; }

  .word-making   { left: 455px; top: 100px; font-size: 74px; color: var(--mint); }
  .word-yourlife { left: 508px; top: 166px; font-size: 44px; color: var(--slate); }
  .word-easier   { left: 622px; top: 198px; font-size: 58px; color: var(--sun); }
  .word-theirs   { left: 420px; top: 232px; font-size: 76px; color: var(--tangerine); }
  .word-helthier { left: 568px; top: 305px; font-size: 100px; color: var(--mint); }
  .word-and      { left: 848px; top: 388px; font-size: 64px; color: var(--stone); }
  .word-happier  { left: 455px; top: 415px; font-size: 92px; color: var(--lime); }

  .brand {
    position: absolute;
    left: 1030px;
    top: 470px;
    display: flex;
    flex-direction: column;
    align-items: center;
    gap: 6px;
  }
  .brand-mark {
    width: 34px;
    height: 34px;
    border-radius: 50%;
    background: var(--logo-grey);
  }
  .brand-name {
    font-family: "Open Sans", Arial, sans-serif;
    font-weight: 400;
    font-size: 17px;
    color: var(--logo-grey);
  }
</style>
</head>
<body>
  <main class="cover">
    <svg class="rope-photo" width="820" height="80" viewBox="0 0 820 80" role="img" aria-label="Photo of a twisted rope stretched across the top">
      <defs>
        <linearGradient id="ropeTone" x1="0" y1="0" x2="0" y2="1">
          <stop offset="0" stop-color="var(--rope-light)"/>
          <stop offset="1" stop-color="var(--rope-dark)"/>
        </linearGradient>
      </defs>
      <polygon points="0,40 810,0 815,10 0,52" fill="url(#ropeTone)"/>
    </svg>

    <svg class="kitten-photo" width="380" height="440" viewBox="0 0 380 440" role="img" aria-label="Photo of a grey tabby kitten hanging from the rope by its front paws">
      <defs>
        <linearGradient id="furTone" x1="0" y1="0" x2="1" y2="1">
          <stop offset="0" stop-color="var(--fur-light)"/>
          <stop offset="1" stop-color="var(--fur-dark)"/>
        </linearGradient>
      </defs>
      <rect x="95" y="45" width="270" height="390" rx="40" fill="url(#furTone)"/>
    </svg>

    <h1 class="slogan" aria-label="Making your life easier, theirs helthier and happier.">
      <span class="display word-making">Making</span>
      <span class="light word-yourlife">your life</span>
      <span class="display-italic word-easier">easier,</span>
      <span class="light word-theirs">theirs</span>
      <span class="display word-helthier">helthier</span>
      <span class="display-italic word-and">and</span>
      <span class="display-italic word-happier">happier.</span>
    </h1>

    <div class="brand">
      <span class="brand-mark"></span>
      <span class="brand-name">BriskTail</span>
    </div>
  </main>
</body>
</html>
```